RM dental business card. A family dental practice.

Logo plus the following details.

RM Dental
Dr. Gareth Moulton D.D.S
Family. Implant.Cosmetic

84 Birchfall Crescent, Unit 12-13
Markham, ON L6P2K8

Tel: 905-555-0183
Fx:905-555-0147
rmdentalcare.example

On the double side:

Next app: ______________________

Please notify us at least 48hours in advance to avoid cancellation fees.

Reason: I didn't get time to view the design. The deadline is extended Mar22nd. Thank you.

Target Market(s)

Family Dental Services

Industry/Entity Type

Dental

Contact Information for Business Card

Put logo prominently and all the info along with it.

Font styles to use
Other font styles liked:
• See Logo Font

Colors
0255a3
3277b5
85acd3
00a990
33b8a4

Requirements
Must have
• Logo and the info stated above.
• See the logo color scheme.
• Or a grayscale (Black, white gray) combination
Nice to have
• A modern unique layout
Should not have
• too simple a design

```html
<!DOCTYPE html>
<html lang="en">
<head>
<meta charset="utf-8">
<title>RM Dental – Business Card</title>
<link rel="stylesheet" href="https://fonts.googleapis.com/css2?family=Alegreya+Sans:ital,wght@0,400;0,500;0,700;1,400&display=swap">
<style>
  :root {
    --navy: #1d3b6e;
    --brand-blue: #0255a3;
    --mid-blue: #3277b5;
    --light-blue: #85acd3;
    --teal: #00a990;
    --teal-light: #33b8a4;
    --ink: #3a3a3a;
    --paper: #ffffff;
    --backdrop: #e6e6e6;
  }
  html, body {
    margin: 0;
    width: 1200px;
    height: 987px;
    overflow: hidden;
    background: var(--backdrop);
    font-family: "Alegreya Sans", sans-serif;
  }
  .canvas { position: relative; width: 1200px; height: 987px; }
  .card {
    position: absolute;
    top: 343px;
    width: 526px;
    height: 300px;
    background: var(--paper);
    border-radius: 16px;
    overflow: hidden;
  }
  .card--front { left: 67px; }
  .card--back { left: 607px; }

  .brand-name {
    position: absolute;
    margin: 0;
    font-weight: 400;
    color: var(--brand-blue);
    line-height: 1;
    white-space: nowrap;
  }
  .tagline {
    position: absolute;
    margin: 0;
    font-weight: 400;
    color: var(--mid-blue);
    white-space: nowrap;
    line-height: 1;
  }
  .card--front .brand-name { left: 54px; top: 16px; font-size: 37px; }
  .card--front .tagline { left: 34px; top: 53px; font-size: 16px; }

  .accent-bar {
    position: absolute; left: 0; top: 92px; width: 9px; height: 36px;
    background: linear-gradient(180deg, var(--teal-light), var(--brand-blue));
  }
  .doctor {
    position: absolute; left: 37px; top: 95px; margin: 0;
    font-size: 20px; font-weight: 700; color: var(--navy); line-height: 1;
  }
  .doctor .credential { font-size: 16px; font-weight: 500; }
  .specialties {
    position: absolute; left: 37px; top: 119px; margin: 0;
    font-size: 17px; font-weight: 400; color: var(--mid-blue); line-height: 1;
  }
  .contact-list {
    position: absolute; left: 37px; top: 148px; margin: 0; padding: 0;
    list-style: none; font-size: 15px; color: var(--ink);
  }
  .contact-list li { display: flex; align-items: center; height: 20.5px; }
  .contact-list svg { width: 13px; height: 13px; margin-right: 10px; fill: var(--navy); }
  .address {
    position: absolute; left: 37px; top: 218px; margin: 0;
    font-style: normal; font-size: 15px; color: var(--ink); line-height: 19px;
  }
  .emblem-field {
    position: absolute; width: 330px; height: 330px; border-radius: 50%;
    background: radial-gradient(circle at 50% 45%, var(--teal-light) 0%, var(--mid-blue) 55%, var(--navy) 100%);
    opacity: 0.9;
  }
  .card--front .emblem-field { left: 361px; top: -17px; }
  .card--back .emblem-field { left: -178px; top: -17px; }

  .brand-lockup .brand-dot {
    position: absolute; left: 193px; top: 43px; width: 76px; height: 76px;
    border-radius: 50%; background: var(--brand-blue);
  }
  .card--back .brand-name { left: 302px; top: 56px; font-size: 33px; }
  .card--back .tagline { left: 286px; top: 88px; font-size: 15px; }

  .appointment-label {
    position: absolute; left: 160px; width: 338px; top: 200px; margin: 0;
    text-align: center; font-size: 21px; font-weight: 700; color: var(--navy); line-height: 1;
  }
  .appointment-line {
    position: absolute; left: 160px; width: 338px; top: 250px; height: 1px; background: #888;
  }
  .cancellation-note {
    position: absolute; left: 150px; width: 360px; top: 258px; margin: 0;
    text-align: center; font-size: 11px; font-style: italic; color: #555; line-height: 14px;
  }
</style>
</head>
<body>
<main class="canvas">
  <section class="card card--front" aria-label="Business card front">
    <div class="emblem-field" role="img" aria-label="Brand emblem area"></div>
    <h1 class="brand-name">RM Dental</h1>
    <p class="tagline">Gentle care for your whole family</p>
    <span class="accent-bar"></span>
    <h2 class="doctor">Dr. Gareth Moulton <span class="credential">D.D.S</span></h2>
    <p class="specialties">Family. Implant. Cosmetic</p>
    <ul class="contact-list">
      <li><svg viewBox="0 0 24 24" aria-hidden="true"><path d="M6.6 10.8a15 15 0 0 0 6.6 6.6l2.2-2.2a1 1 0 0 1 1-.25 11.4 11.4 0 0 0 3.6.57 1 1 0 0 1 1 1V20a1 1 0 0 1-1 1A17 17 0 0 1 3 4a1 1 0 0 1 1-1h3.5a1 1 0 0 1 1 1c0 1.25.2 2.45.57 3.57a1 1 0 0 1-.25 1z"/></svg>905-555-0183</li>
      <li><svg viewBox="0 0 24 24" aria-hidden="true"><path d="M7 2h10v5H7zM4 8h16a2 2 0 0 1 2 2v7h-4v5H6v-5H2v-7a2 2 0 0 1 2-2zm4 9v3h8v-3z"/></svg>905-555-0147</li>
      <li><svg viewBox="0 0 24 24" aria-hidden="true"><path d="M12 2a10 10 0 1 0 0 20 10 10 0 0 0 0-20zm-1 17.9A8 8 0 0 1 4.1 11H7c0 3 1.5 5 4 5zM13 4.1A8 8 0 0 1 19.9 11H16c0-3-1-5-3-6.9zM9 9l2-3 2 3-1 3 3 2-1 3-3-2-2 2z"/></svg>rmdentalcare.example</li>
    </ul>
    <address class="address">84 Birchfall Crescent<br>Unit 12-13<br>Markham, ON L6P2K8</address>
  </section>

  <section class="card card--back" aria-label="Business card back">
    <div class="emblem-field" role="img" aria-label="Brand emblem area"></div>
    <div class="brand-lockup">
      <span class="brand-dot"></span>
      <h2 class="brand-name">RM Dental</h2>
      <p class="tagline">Gentle care for your whole family</p>
    </div>
    <p class="appointment-label">Next Appointment</p>
    <span class="appointment-line"></span>
    <p class="cancellation-note">Please notify us at least 48hours in advance to avoid cancellation fees.</p>
  </section>
</main>
</body>
</html>
```